Business card

would like a double sided business card made up with my logos provided.
Prefer card to have black background and to use the black logos, with matching blue writing for the text.
One side to just be the logo, (Try to use both the black logos)
the other side to have the logo and also my credentials/business information.

Covering all aspects of Carpentry and Building Services

Marcus Thelwin
Qualified Carpenter
Mob: 0417263985
Email: rkt.joinery@fernmail.example
ABN: 47 619 283 504

Industry/Entity Type

Business

Contact Information for Business Card

Marcus Thelwin
Qualified Carpenter
Mob: 0417263985
ABN: 47 619 283 504

Requirements
Must have
• Please try to use both the black logos and incorporate into the card.

```html
<!DOCTYPE html>
<html lang="en">
<head>
<meta charset="utf-8">
<title>RKT Joinery – Business Card</title>
<link rel="stylesheet" href="https://fonts.googleapis.com/css2?family=Lato:wght@400;700;900&family=Arimo:ital,wght@0,700;1,700&display=swap">
<style>
  :root {
    --backdrop: #6d6d6d;
    --card-black: #0b0b0c;
    --card-white: #f1f1f0;
    --band-grey: #2e2e30;
    --brand-blue: #1aa3dc;
    --logo-white: #eeeeee;
    --faint-grey: #dcdcdc;
    --body-white: #f5f5f5;
  }
  * { box-sizing: border-box; margin: 0; padding: 0; }
  html, body { width: 1200px; height: 955px; overflow: hidden; }
  body {
    background: var(--backdrop);
    font-family: "Lato", Arial, sans-serif;
    display: flex;
    align-items: center;
    justify-content: center;
    gap: 48px;
  }
  .card {
    position: relative;
    width: 540px;
    height: 309px;
    border-radius: 3px;
    overflow: hidden;
    box-shadow: 0 10px 26px rgba(0,0,0,0.35);
  }

  /* Front: logo side */
  .card--front {
    background: var(--card-black);
    display: flex;
    flex-direction: column;
    align-items: center;
    justify-content: center;
  }
  .brand-mark {
    display: flex;
    align-items: center;
    gap: 14px;
    margin-bottom: 44px;
  }
  .brand-mark__square {
    width: 22px;
    height: 22px;
    background: var(--brand-blue);
  }
  .brand-mark__name {
    font-weight: 900;
    font-size: 50px;
    letter-spacing: 2px;
    color: var(--logo-white);
    text-transform: uppercase;
  }
  .front__tagline {
    position: absolute;
    bottom: 30px;
    left: 0;
    right: 0;
    text-align: center;
    font-family: "Arimo", Arial, sans-serif;
    font-weight: 700;
    font-size: 15px;
    color: var(--brand-blue);
  }

  /* Back: details side */
  .card--back { background: var(--card-white); }
  .back__shape { position: absolute; inset: 0; width: 100%; height: 100%; }
  .back__header {
    position: absolute;
    top: 22px;
    left: 24px;
  }
  .back__brand {
    font-weight: 900;
    font-size: 28px;
    letter-spacing: 1px;
    color: var(--logo-white);
    text-transform: uppercase;
  }
  .back__person { margin-top: 12px; }
  .back__name {
    font-weight: 700;
    font-size: 15px;
    color: var(--brand-blue);
  }
  .back__role {
    font-size: 11px;
    color: var(--body-white);
    margin-top: 2px;
  }
  .back__watermark {
    position: absolute;
    right: 70px;
    top: 150px;
    width: 70px;
    height: 70px;
    background: var(--faint-grey);
  }
  .contact-list {
    position: absolute;
    right: 18px;
    bottom: 22px;
    list-style: none;
    text-align: right;
  }
  .contact-list__item {
    display: flex;
    align-items: center;
    justify-content: flex-end;
    gap: 8px;
    font-size: 14px;
    line-height: 19px;
    color: var(--brand-blue);
  }
  .contact-list__icon {
    width: 13px;
    height: 13px;
    flex: none;
  }
</style>
</head>
<body>

  <section class="card card--front" aria-label="Card front">
    <div class="brand-mark">
      <span class="brand-mark__square"></span>
      <span class="brand-mark__name">RKT Joinery</span>
    </div>
    <p class="front__tagline">Covering all aspects of Carpentry and Building Services</p>
  </section>

  <section class="card card--back" aria-label="Card back">
    <svg class="back__shape" viewBox="0 0 540 309" preserveAspectRatio="none" aria-hidden="true">
      <polygon points="0,0 540,0 540,150 0,240" fill="var(--band-grey)"/>
      <polygon points="0,0 540,0 540,138 0,228" fill="var(--card-black)"/>
      <line x1="0" y1="249" x2="540" y2="159" stroke="var(--brand-blue)" stroke-width="2"/>
    </svg>

    <header class="back__header">
      <div class="back__brand">RKT Joinery</div>
      <div class="back__person">
        <p class="back__name">Marcus Thelwin</p>
        <p class="back__role">Qualified Carpenter</p>
      </div>
    </header>

    <div class="back__watermark" aria-hidden="true"></div>

    <ul class="contact-list">
      <li class="contact-list__item">
        <span>0417263985</span>
        <svg class="contact-list__icon" viewBox="0 0 13 13" aria-hidden="true">
          <rect width="13" height="13" fill="#111"/>
          <rect x="4" y="2" width="5" height="9" rx="1" fill="none" stroke="#fff" stroke-width="1.2"/>
        </svg>
      </li>
      <li class="contact-list__item">
        <span>ABN: 47 619 283 504</span>
        <svg class="contact-list__icon" viewBox="0 0 13 13" aria-hidden="true">
          <rect width="13" height="13" fill="#111"/>
          <path d="M2.5 6.5 L6.5 2.5 L10.5 6.5 M4 6 V10.5 H9 V6" fill="none" stroke="#fff" stroke-width="1.2"/>
        </svg>
      </li>
      <li class="contact-list__item">
        <span>rkt.joinery@fernmail.example</span>
        <svg class="contact-list__icon" viewBox="0 0 13 13" aria-hidden="true">
          <rect width="13" height="13" fill="#111"/>
          <rect x="2.5" y="4" width="8" height="5.5" fill="none" stroke="#fff" stroke-width="1.1"/>
          <path d="M2.5 4 L6.5 7 L10.5 4" fill="none" stroke="#fff" stroke-width="1.1"/>
        </svg>
      </li>
    </ul>
  </section>

</body>
</html>
```